Fast quick flyer for Merchant Showcase Fair

I am an information security consultant that needs to have a flyer and QUICK!!!
I need to get it to the printer today to have if done by monday. Quick turnaound.
I don't need the most amazing flyer but something that will capture their attention and offer them 40% off my base rate.
Updates

Here's some slight updates to the text, can you update and incorporate (PS: For some reason, when I initially put in Luvaro Systems, a " (quote) showed up, it's an apostrophe ( Luvaro Systems): Text: Luvaro Systems is the information security department for small and mid-sized businesses. Leveraging our 20+ years of information security experience, we will bring you the same level of service found at Pinnacle 400 companies. Small and mid-sized companies are often the target of malicious activity because they tend to lack the expertise to properly secure their environments. Now you can have your very own information security department at a fraction of the cost of a full time staff. Our typical rate for our premium offering: Shieldwise Direct is $5000/month based on a signed one year commitment. But for expo attendees, we are offering a special discount. As an expo attendee, you are eligible for a 40% discount. Shieldwise Direct for expo attendees will be $3000/month based on a signed one year commitment. Why put your company and your business at risk. Luvaro Systems is here to secure your company's future! Contact us now for more information: Martin Kessell Luvaro Systems "The information security department of small and mid-sized companies" 555-318-7702 info@luvarosys.example http://www.luvarosys.example

Also, this is going to be a 6x9 heavy stock postcard

Addition: Promo Code: TradeFairPass 2014

Target Market(s)

Small businesses with a small IT department that can't afford to hire a full time IT Security Staff. We are the outsourced Information Security group

Industry/Entity Type

Small Business

Colors

Designer to choose colors to be used in the design.

Requirements
Must have
• Sell the idea that they need to take security serious and that we are the ones to do the job

Should stress that because they are attendees of the Merchant Showcase Fair, they are eligible to get a 40% discount on our standard rate

```html
<!DOCTYPE html>
<html lang="en">
<head>
<meta charset="utf-8">
<title>Luvaro Systems – Merchant Showcase Fair Flyer</title>
<link rel="stylesheet" href="https://fonts.googleapis.com/css2?family=Open+Sans:wght@400;600;700&family=Tinos:wght@400;700&display=swap">
<style>
  :root {
    --backdrop: #4d575c;
    --paper: #ffffff;
    --navy: #141a5e;
    --ink: #1b2c46;
    --slate: #4f5a60;
    --offer-red: #e8141b;
    --text: #1e1e1e;
    --visual-light: #ffffff;
    --visual-mid: #e4e6ec;
    --visual-accent: #aab4f0;
  }
  * { margin: 0; padding: 0; box-sizing: border-box; }
  html, body {
    width: 1000px; height: 1200px; overflow: hidden;
    background: var(--backdrop);
    font-family: "Open Sans", Arial, sans-serif;
  }
  .flyer {
    position: absolute; left: 134px; top: 126px;
    width: 732px; height: 948px;
    background: var(--paper);
    overflow: hidden;
  }
  .tagline-band {
    position: absolute; left: 0; top: 0; width: 100%; height: 72px;
    background: var(--navy); color: #fff;
    font-family: "Tinos", "Times New Roman", serif;
    font-size: 27px; letter-spacing: 0.5px;
    display: flex; align-items: center; justify-content: center;
  }
  .tagline-band strong { font-weight: 700; }
  .brand {
    position: absolute; top: 118px; left: 0; width: 100%;
    display: flex; align-items: center; justify-content: center; gap: 14px;
  }
  .brand-mark { width: 46px; height: 46px; background: var(--navy); }
  .brand-name {
    font-size: 34px; font-weight: 600; color: var(--navy);
    letter-spacing: 1px; text-transform: uppercase; line-height: 1;
  }
  .event-title {
    position: absolute; top: 212px; left: 0; width: 100%;
    text-align: center; color: var(--ink);
    font-size: 33px; font-weight: 400; letter-spacing: 0.3px;
  }
  .event-intro {
    position: absolute; top: 260px; left: 60px; width: 612px;
    text-align: center; color: var(--ink);
    font-size: 16px; line-height: 22px; text-transform: uppercase;
  }
  .hero-visual {
    position: absolute; left: 0; top: 318px; width: 440px; height: 378px;
    background: radial-gradient(ellipse at 55% 45%, var(--visual-light) 0%, var(--visual-light) 40%, var(--visual-mid) 100%);
  }
  .hero-visual::after {
    content: ""; position: absolute; left: 40px; top: 80px; width: 280px; height: 220px;
    background: radial-gradient(ellipse at center, rgba(170,180,240,0.55) 0%, rgba(170,180,240,0) 70%);
  }
  .pitch {
    position: absolute; left: 440px; top: 360px; width: 262px;
    text-align: center; color: var(--text);
    font-size: 14.5px; line-height: 20.5px;
  }
  .pitch p + p { margin-top: 20px; }
  .join-cta {
    position: absolute; left: 484px; top: 632px;
    font-size: 33px; font-weight: 700; color: var(--text);
  }
  .discount-bands { position: absolute; left: 0; top: 674px; }
  .offer-banner {
    position: absolute; left: 10px; top: 698px; color: #fff;
    font-size: 21px; line-height: 23px;
  }
  .offer-banner .line-two { padding-left: 70px; }
  .offer-banner strong { font-weight: 700; }
  .discount-figure {
    position: absolute; left: 568px; top: 682px;
    font-size: 58px; font-weight: 700; color: #fff; line-height: 1;
  }
  .rate-note {
    position: absolute; top: 770px; left: 0; width: 100%;
    text-align: center; font-size: 14.5px; color: var(--text);
  }
  .expo-rate {
    position: absolute; top: 794px; left: 0; width: 100%;
    text-align: center; font-size: 14.5px; color: var(--text);
  }
  .expo-rate strong { font-size: 22px; font-weight: 700; color: var(--offer-red); }
  .contact-line {
    position: absolute; top: 836px; left: 0; width: 100%;
    display: flex; align-items: baseline; justify-content: center; gap: 18px;
  }
  .contact-name { font-size: 25px; font-weight: 700; color: var(--navy); }
  .contact-phone { font-size: 38px; color: var(--text); }
  .footer-band {
    position: absolute; left: 0; bottom: 0; width: 100%; height: 54px;
    background: var(--slate); color: #fff; font-size: 18px;
    display: flex; align-items: center;
  }
  .footer-email { position: absolute; left: 82px; }
  .footer-web { position: absolute; left: 460px; }
</style>
</head>
<body>
  <main class="flyer">
    <header class="tagline-band">SECURING THE&nbsp;<strong>FUTURE</strong>&nbsp;OF YOUR COMPANY</header>

    <div class="brand">
      <span class="brand-mark"></span>
      <span class="brand-name">Luvaro Systems</span>
    </div>

    <h1 class="event-title">SMALL BUSINESS CONFERENCE/EXPO</h1>
    <p class="event-intro">Introduce Luvaro Systems as a information security<br>department for small and mid-sized businesses.</p>

    <div class="hero-visual" role="img" aria-label="Silver key inserted into a blue puzzle piece"></div>

    <section class="pitch">
      <p>Small companies are targets because they lack the expertise at information security that large companies have.</p>
      <p>We have over 20 years of information security experience and we can leverage our expertise to give small companies the same level of security experience that Pinnacle 400 companies have.</p>
    </section>

    <div class="join-cta">Join Us Now</div>

    <svg class="discount-bands" width="732" height="84" viewBox="0 0 732 84" aria-hidden="true">
      <polygon points="0,22 500,22 550,84 0,84" fill="var(--navy)"/>
      <polygon points="484,0 732,0 732,84 550,84" fill="var(--slate)"/>
    </svg>

    <div class="offer-banner">
      <div>For expo attendees,</div>
      <div class="line-two">we are offering a <strong>SPECIAL DISCOUNT.</strong></div>
    </div>
    <div class="discount-figure">40%</div>

    <p class="rate-note">Our monthly rate is $5000 (one year contract).&nbsp; For Expo attendees, we are offering a 40% discount.</p>
    <p class="expo-rate"><strong>Special Expo rate of $3000/month</strong> (one year contract).</p>

    <div class="contact-line">
      <span class="contact-name">MARTIN KESSELL</span>
      <span class="contact-phone">555-318-7702</span>
    </div>

    <footer class="footer-band">
      <span class="footer-email">martin.kessell@luvarosys.example</span>
      <span class="footer-web">www.luvarosys.example</span>
    </footer>
  </main>
</body>
</html>
```